Recruitment website for new startup company - Calder Ashby Recruitment

Hi , I need to design a web page for my new recruitment company with the ability to link to social media accounts. The ability to add and remove job posts along with a blog page which I can update. More importantly I need the website to have the functionality of applicants being able to upload their cv and somewhere for me to store it. I will need assistance/recommendation for email address with company name, hosting and security. An about us page. The website will also need a search function for applicants to narrow down the search. Again I will need to be able to update this myself as the company grows. I have my logo ready domain address ready and would like the web site done ASAP. Thank you for your help.
Updates

Reason: Want to get a few more ideas and variations to designs done. But using logo as inspiration Thanks

Target Market(s)

Financial and property industry so professionals. New starters to senior management age range 25-60

Industry/Entity Type

Financial

Coding

Coded - Design and coding required

Number of Pages Required

4 page

Colors

Designer to choose colors to be used in the design.

Requirements
Must have
• Ability for me to add amend and remove job posts, ability for applicants to upload cv and for me to store and access it. Link to social media accounts
Should not have
• Needs to be clean approachable so not to childish but must come across as approachable and trustworthy.
• No yellow please my logo has a gold V not yellow. If it looks yellow use a different colour please. Thanks

```html
<!DOCTYPE html>
<html lang="en">
<head>
<meta charset="utf-8">
<title>Calder Ashby Recruitment</title>
<link href="https://fonts.googleapis.com/css2?family=Poppins:wght@300;400;500;600;700&display=swap" rel="stylesheet">
<style>
:root{
  --navy:#1f3a6e;
  --navy-dark:#17305c;
  --gold:#c9a43a;
  --gold-soft:#d6b04a;
  --ink:#1f3a6e;
  --text:#555c68;
  --muted:#8a909a;
  --line:#d7dbe2;
  --row-hl:#d9dce1;
  --white:#ffffff;
}
*{box-sizing:border-box;margin:0;padding:0}
html,body{width:1200px;height:3852px;overflow:hidden}
body{font-family:'Poppins',sans-serif;color:var(--text);background:var(--white);position:relative}
a{color:inherit;text-decoration:none}

/* hero */
.hero{position:absolute;left:0;top:0;width:1200px;height:600px;overflow:hidden}
.hero-photo{position:absolute;inset:0;background:linear-gradient(160deg,#5d7fae 0%,#3c5f93 40%,#2a4b80 75%,#24437a 100%)}
.hero-shade{position:absolute;inset:0;background:linear-gradient(180deg,rgba(20,40,80,.35),rgba(20,40,80,.1) 60%,rgba(20,40,80,.3))}
.hero-curve{position:absolute;left:0;bottom:0;width:1200px;height:140px}
.topbar{position:absolute;top:0;right:0;left:0;height:30px;display:flex;justify-content:flex-end;align-items:center;gap:18px;padding-right:50px;font-size:13px;color:var(--white)}
.topbar .sep{opacity:.8}
.dot-social{width:12px;height:12px;border-radius:50%;background:var(--white);display:inline-block}
.brand{position:absolute;left:100px;top:52px;color:var(--white);font-weight:600;font-size:22px;line-height:1.05;letter-spacing:1px}
.brand small{display:block;font-size:12px;letter-spacing:3px;font-weight:400}
.nav{position:absolute;left:320px;top:64px;display:flex;gap:24px;font-size:13px;color:var(--white);text-transform:uppercase}
.login{position:absolute;left:762px;top:64px;font-size:13px;color:var(--white)}
.cv-btn{position:absolute;left:997px;top:50px;width:160px;height:44px;border:2px solid var(--gold-soft);border-radius:22px;color:var(--gold-soft);font-weight:600;font-size:15px;display:flex;align-items:center;justify-content:center}
.hero h1{position:absolute;top:290px;left:0;width:1200px;text-align:center;color:var(--gold-soft);font-size:37px;font-weight:600}
.hero .lead{position:absolute;top:338px;left:0;width:1200px;text-align:center;color:var(--white);font-size:14px}
.search{position:absolute;left:228px;top:384px;width:742px;height:44px;background:var(--white);border-radius:22px;display:flex;align-items:center;font-size:14px;color:var(--muted)}
.search .field{display:flex;align-items:center;gap:8px;padding-left:26px;height:24px}
.search .f1{width:265px;border-right:1px solid var(--line)}
.search .f2{width:172px;border-right:1px solid var(--line)}
.search .f3{width:170px}
.search .go{position:absolute;right:8px;top:5px;width:120px;height:34px;border-radius:6px;background:var(--gold-soft);color:var(--white);font-weight:600;display:flex;align-items:center;justify-content:center;gap:6px}

/* steps */
.intro h2{position:absolute;top:705px;left:0;width:1200px;text-align:center;color:var(--navy);font-size:34px;font-weight:700}
.intro h2 .hl{color:var(--gold-soft);text-decoration:underline;text-underline-offset:6px}
.intro .sub{position:absolute;top:765px;left:0;width:1200px;text-align:center;font-size:16px}
.step{position:absolute;top:860px;width:300px;text-align:center}
.step .ring{width:116px;height:116px;border:3px solid var(--gold-soft);border-radius:50%;margin:0 auto;position:relative;display:flex;align-items:center;justify-content:center}
.step .num{position:absolute;right:-10px;top:-6px;width:34px;height:34px;border-radius:50%;background:var(--gold-soft);color:var(--white);font-weight:600;font-size:15px;display:flex;align-items:center;justify-content:center}
.step h3{margin-top:30px;color:var(--navy);font-size:27px;font-weight:700}
.step p{margin:20px auto 0;width:270px;text-align:left;font-size:13px;line-height:2.1}
.flow{position:absolute}

/* jobs */
.sec-title{position:absolute;color:var(--navy);font-size:27px;font-weight:700}
.pager{position:absolute;display:flex;gap:10px;align-items:center}
.pager span{width:28px;height:28px;display:flex;align-items:center;justify-content:center;font-size:14px;color:var(--muted)}
.pager .on{background:var(--gold-soft);color:var(--white)}
.jobs{position:absolute;left:157px;top:1284px;width:575px;height:570px;border:1px solid var(--line)}
.job{height:114px;border-bottom:1px solid var(--line);padding:26px 30px 0;position:relative}
.job:last-child{border-bottom:0}
.job.active{background:var(--row-hl)}
.job h4{color:var(--navy);font-size:20px;font-weight:400}
.job .meta{margin-top:10px;font-size:12px;color:var(--text);display:flex;gap:18px}
.tag{position:absolute;right:22px;top:30px;background:var(--gold-soft);color:var(--white);font-size:11px;font-weight:600;padding:2px 12px;border-radius:10px}
.ago{position:absolute;right:22px;top:62px;font-size:12px}
.featured{position:absolute;left:763px;top:1284px;width:277px;height:562px;border:1px solid var(--line)}
.featured .photo{height:228px;background:linear-gradient(135deg,#b9c9d8,#7f9ab6 55%,#5c7898)}
.featured .body{padding:22px 22px 0}
.featured h4{color:var(--navy);font-size:18px;font-weight:700;line-height:1.45}
.featured .tag{position:static;display:inline-block;margin-top:12px}
.featured .loc{margin-top:12px;font-size:12px}
.featured p{margin-top:12px;font-size:11.5px;line-height:1.75}
.apply{display:block;margin:18px auto 0;width:172px;height:34px;border-radius:17px;background:var(--navy);color:var(--white);font-size:13px;font-weight:600;text-align:center;line-height:34px}
.dots{display:flex;gap:7px;justify-content:center;margin-top:26px}
.dots i{width:7px;height:7px;border-radius:50%;background:#dcdfe4}
.dots i:first-child{background:var(--gold-soft)}
.pill{position:absolute;height:42px;border:2px solid var(--navy);border-radius:21px;color:var(--navy);font-weight:600;font-size:15px;display:flex;align-items:center;justify-content:center;gap:8px}

/* bands */
.cta-band{position:absolute;left:0;top:1990px;width:1200px;height:85px;background:var(--gold-soft);color:var(--white)}
.cta-band p{position:absolute;left:232px;top:30px;font-size:17px}
.cta-band a{position:absolute;left:807px;top:22px;width:162px;height:40px;border:2px solid var(--white);border-radius:20px;font-size:13px;font-weight:600;display:flex;align-items:center;justify-content:center}
.refer{position:absolute;left:0;top:2075px;width:1200px;height:495px;background:linear-gradient(100deg,#1e3461 0%,#3d557f 45%,#60789d 70%,#3a5079 100%);color:var(--white);text-align:center}
.refer h2{position:absolute;top:160px;left:0;width:1200px;font-size:39px;font-weight:700;line-height:1.3}
.refer p{position:absolute;top:265px;left:0;width:1200px;font-size:15px;line-height:1.9}
.refer a{position:absolute;left:541px;top:335px;width:170px;height:42px;border:2px solid var(--gold-soft);border-radius:21px;color:var(--gold-soft);font-size:13px;font-weight:600;display:flex;align-items:center;justify-content:center}

/* blog */
.blog h2{position:absolute;top:2620px;left:0;width:1200px;text-align:center;color:var(--navy);font-size:32px;font-weight:700}
.blog h2 span{color:var(--gold-soft)}
.blog .sub{position:absolute;top:2688px;left:255px;width:690px;text-align:center;font-size:13px;line-height:2.3}
.post{position:absolute;top:2786px;width:463px}
.post .photo{height:214px}
.post .row{display:flex;margin-top:26px}
.post .date{width:70px;text-align:right;color:var(--navy);font-weight:700;font-size:18px;line-height:1.5;padding-right:14px;border-right:2px solid var(--gold-soft)}
.post .row p{padding-left:18px;font-size:13px;line-height:1.9}

/* footer */
.footer{position:absolute;left:0;top:3210px;width:1200px;height:642px}
.footer svg.bg{position:absolute;inset:0}
.f-h{position:absolute;color:var(--gold-soft);font-size:18px;font-weight:600}
.sub-form{position:absolute;left:145px;top:3410px;width:330px;height:36px;display:flex}
.sub-form .in{flex:1;background:var(--white);font-size:12px;color:var(--muted);padding:10px 14px}
.sub-form .btn{width:118px;background:var(--gold-soft);color:var(--white);font-size:12px;font-weight:600;display:flex;align-items:center;justify-content:center}
.socials{position:absolute;left:557px;top:3412px;display:flex;gap:14px}
.socials i{width:30px;height:30px;border:2px solid var(--white);border-radius:50%;display:flex;align-items:center;justify-content:center}
.socials i b{width:16px;height:16px;border-radius:50%;background:var(--gold-soft)}
.call{position:absolute;left:818px;top:3414px;color:var(--white);font-size:14px}
.call strong{font-size:20px;font-weight:700}
.f-brand{position:absolute;left:145px;top:3530px;color:var(--white);font-size:38px;font-weight:500;line-height:1.1;letter-spacing:1px}
.f-brand small{display:block;font-size:20px;letter-spacing:5px;font-weight:400}
.f-about{position:absolute;left:145px;top:3615px;width:200px;color:var(--white);font-size:12px;line-height:1.95}
.f-list{position:absolute;list-style:none;color:var(--white);font-size:13px}
.f-list li{margin-bottom:17px}
.f-list li::before{content:"";display:inline-block;border-left:6px solid var(--white);border-top:4px solid transparent;border-bottom:4px solid transparent;margin-right:8px}
.f-list li.gold{color:var(--gold-soft)}
.f-list li.gold::before{border-left-color:var(--gold-soft)}
.contact-form{position:absolute;left:820px;top:3560px;width:237px}
.contact-form div{background:#e2e4e8;color:var(--muted);font-size:11px;padding:8px 10px;margin-bottom:11px;height:34px}
.contact-form .msg{height:72px;position:relative}
.contact-form .send{position:absolute;right:0;top:0;width:44px;height:72px;background:var(--gold-soft);display:flex;align-items:center;justify-content:center}
.rule{position:absolute;left:145px;top:3755px;width:912px;height:1px;background:rgba(255,255,255,.2)}
.copy{position:absolute;top:3777px;left:0;width:1200px;text-align:center;color:var(--white);font-size:11px}
</style>
</head>
<body>

<header class="hero">
  <div class="hero-photo" role="img" aria-label="Photo of business professionals meeting around a table"></div>
  <div class="hero-shade"></div>
  <div class="topbar">
    <span>✉ info@calderashby.example</span><span class="sep">|</span>
    <span class="dot-social"></span><span class="dot-social"></span><span class="dot-social"></span><span class="dot-social"></span>
  </div>
  <div class="brand">CALDER ASHBY<small>RECRUITMENT</small></div>
  <nav class="nav"><a>Home</a><a>About</a><a>Recruitment</a><a>News</a><a>Contact</a></nav>
  <a class="login">LOGIN / REGISTER &nbsp;➜</a>
  <a class="cv-btn">CV Drop Point</a>
  <h1>Multi-Industry Recruitment Agency</h1>
  <p class="lead">Select your sector and/or type job keywords, then click search to find your perfect job.</p>
  <div class="search">
    <div class="field f1">
      <svg width="14" height="14" viewBox="0 0 14 14"><circle cx="6" cy="6" r="4.5" fill="none" stroke="#8a909a" stroke-width="1.6"/><path d="M9.5 9.5L13 13" stroke="#8a909a" stroke-width="1.6"/></svg>Job Keywords</div>
    <div class="field f2">
      <svg width="11" height="14" viewBox="0 0 11 14"><path d="M5.5 13S1 8 1 5a4.5 4.5 0 0 1 9 0c0 3-4.5 8-4.5 8z" fill="none" stroke="#8a909a" stroke-width="1.4"/></svg>Location</div>
    <div class="field f3">
      <svg width="13" height="13" viewBox="0 0 13 13"><circle cx="6.5" cy="3.5" r="3" fill="#8a909a"/><path d="M1 13a5.5 5 0 0 1 11 0z" fill="#8a909a"/></svg>Sector</div>
    <a class="go"><svg width="12" height="12" viewBox="0 0 14 14"><circle cx="6" cy="6" r="4.5" fill="none" stroke="#fff" stroke-width="2"/><path d="M9.5 9.5L13 13" stroke="#fff" stroke-width="2"/></svg>Search</a>
  </div>
  <svg class="hero-curve" viewBox="0 0 1200 140" preserveAspectRatio="none"><path d="M0 70 Q600 170 1200 0 L1200 140 L0 140Z" fill="#fff"/></svg>
</header>

<section class="intro">
  <h2>All the jobs you want in <span class="hl">one</span> simple place.</h2>
  <p class="sub">Find the jobs you want in just a few simple quicks.</p>

  <div class="step" style="left:138px">
    <div class="ring"><span class="num">1</span>
      <svg width="46" height="46" viewBox="0 0 46 46"><circle cx="19" cy="19" r="14" fill="none" stroke="#c9a43a" stroke-width="6"/><path d="M29 29l12 12" stroke="#c9a43a" stroke-width="7" stroke-linecap="round"/></svg></div>
    <h3>Search</h3>
    <p>In enim justo, rhoncus ut, imperdiet a, venenatis vitae, justo. Nullam dictum felis eu pede mollis pretium.</p>
  </div>
  <div class="step" style="left:451px">
    <div class="ring"><span class="num">2</span>
      <svg width="48" height="48" viewBox="0 0 48 48"><rect x="6" y="10" width="30" height="30" fill="none" stroke="#c9a43a" stroke-width="2.5"/><path d="M18 30l2-7 18-18 5 5-18 18z" fill="none" stroke="#c9a43a" stroke-width="2.5"/></svg></div>
    <h3>Apply</h3>
    <p>In enim justo, rhoncus ut, imperdiet a, venenatis vitae, justo. Nullam dictum felis eu pede mollis pretium.</p>
  </div>
  <div class="step" style="left:767px">
    <div class="ring"><span class="num">3</span>
      <svg width="52" height="52" viewBox="0 0 52 52"><circle cx="26" cy="15" r="10" fill="none" stroke="#c9a43a" stroke-width="2"/><path d="M6 48c0-12 9-19 20-19s20 7 20 19z" fill="none" stroke="#c9a43a" stroke-width="2"/><path d="M26 29l-4 8 4 9 4-9z" fill="none" stroke="#c9a43a" stroke-width="2"/></svg></div>
    <h3>Hired</h3>
    <p>In enim justo, rhoncus ut, imperdiet a, venenatis vitae, justo. Nullam dictum felis eu pede mollis pretium.</p>
  </div>
  <svg class="flow" style="left:408px;top:893px" width="70" height="30" viewBox="0 0 70 30"><path d="M2 20 Q30 -4 62 14" fill="none" stroke="#1f3a6e" stroke-width="1.5"/><path d="M56 8l7 6-9 3" fill="none" stroke="#1f3a6e" stroke-width="1.5"/></svg>
  <svg class="flow" style="left:720px;top:935px" width="70" height="30" viewBox="0 0 70 30"><path d="M2 10 Q30 34 62 14" fill="none" stroke="#1f3a6e" stroke-width="1.5"/><path d="M54 12l9 2-5 8" fill="none" stroke="#1f3a6e" stroke-width="1.5"/></svg>
</section>

<section class="jobs-area">
  <h2 class="sec-title" style="left:157px;top:1232px">Recent Jobs</h2>
  <div class="pager" style="left:676px;top:1236px"><span>‹</span><span class="on">›</span></div>
  <h2 class="sec-title" style="left:763px;top:1232px">Featured Jobs</h2>

  <div class="jobs">
    <div class="job"><h4>Sales &amp; Marketing Coordinator</h4><div class="meta"><span>⚲ Germany, Hannover</span><span>ⓔ £27,500</span></div><span class="tag">Full Time</span><span class="ago">Posted 12 hours ago</span></div>
    <div class="job"><h4>Engineering Technician</h4><div class="meta"><span>⚲ Netherlands, Rotterdam</span><span>ⓔ £27,000 - £30,000</span></div><span class="tag">Full Time</span><span class="ago">Posted 18 hours ago</span></div>
    <div class="job active"><h4>Science Teacher</h4><div class="meta"><span>⚲ England, London, Camden</span><span>ⓔ £30,000 - £32,500</span></div><span class="tag">Full Time</span><span class="ago">Posted 2 days ago</span></div>
    <div class="job"><h4>Accounts Assistant</h4><div class="meta"><span>⚲ England, Hampshire, Gosport</span><span>ⓔ £31,900 - £36,970</span></div><span class="tag">Full Time</span><span class="ago">Posted 12 days ago</span></div>
    <div class="job"><h4>Clinical Support Specialist</h4><div class="meta"><span>⚲ Madrid, Spain</span><span>ⓔ £12,900 - £18,970</span></div><span class="tag">Part Time</span><span class="ago">Posted 19 hours ago</span></div>
  </div>

  <article class="featured">
    <div class="photo" role="img" aria-label="Photo of financial charts and a laptop on a desk"></div>
    <div class="body">
      <h4>Account Fraud Prevention Officer</h4>
      <span class="tag">Full Time</span>
      <div class="loc">⚲ Germany, Hannover &nbsp;&nbsp;ⓔ £27,500</div>
      <p>Lorem ipsum dolor sit amet, consectetur adipiscing elit. Nunc a congue magna, non maximus eros. Aliquam erat volutpat. Donec suscipit id ante in pulvinar.</p>
      <a class="apply">Apply for this Job</a>
      <div class="dots"><i></i><i></i><i></i></div>
    </div>
  </article>

  <a class="pill" style="left:370px;top:1880px;width:182px">View all Jobs ›</a>
</section>

<section class="cta-band">
  <p>Add your resume and let your next job find you.</p>
  <a>ADD RESUME</a>
</section>

<section class="refer" role="img" aria-label="Photo of a smiling professional at work in a bright office">
  <h2>Refer a friend and get £250 on<br>successful placement</h2>
  <p>In enim justo, rhoncus ut, imperdiet a, venenatis vitae, justo.<br>Nullam dictum felis eu pede mollis pretium.</p>
  <a>REFER A FRIEND</a>
</section>

<section class="blog">
  <h2>Latest Blogs from <span>CALDER ASHBY</span></h2>
  <p class="sub">In enim justo, rhoncus ut, imperdiet a, venenatis vitae, justo. Nullam dictum felis eu pede mollis pretium. Integer tincidunt. Cras dapibus. Vivamus elementum semper nisi. Aenean vulputate eleifend tellus.</p>
  <article class="post" style="left:123px">
    <div class="photo" role="img" aria-label="Photo of hands reviewing documents at a desk" style="background:linear-gradient(135deg,#c9d3dd,#8fa3b8 60%,#6f86a0)"></div>
    <div class="row"><div class="date">Nov 01,<br>2017</div><p>Etiam ultricies nisi vel augue. Curabitur ullamcorper ultricies tellus eget condimentum nisl.</p></div>
  </article>
  <article class="post" style="left:616px">
    <div class="photo" role="img" aria-label="Photo of a smiling team gathered around a laptop" style="background:linear-gradient(135deg,#e0d2bf,#b99d80 55%,#8c7a68)"></div>
    <div class="row"><div class="date">Oct 11,<br>2017</div><p>Etiam ultricies nisi vel augue. Curabitur ullamcorper ultricies tellus eget condimentum nisl.</p></div>
  </article>
  <a class="pill" style="left:505px;top:3122px;width:185px">Read all News ›</a>
  <div class="pager" style="left:1020px;top:3129px"><span>‹</span><span class="on">›</span></div>
</section>

<footer class="footer">
  <svg class="bg" viewBox="0 0 1200 642" preserveAspectRatio="none"><path d="M0 42 Q600 -30 1200 42 L1200 642 L0 642Z" fill="#1f3a6e"/></svg>
</footer>
<h3 class="f-h" style="left:145px;top:3372px">Subscribe to our Newsletter</h3>
<div class="sub-form"><div class="in">Your email address</div><div class="btn">➤ SUBSCRIBE</div></div>
<h3 class="f-h" style="left:557px;top:3372px">Follow us on</h3>
<div class="socials"><i><b></b></i><i><b></b></i><i><b></b></i><i><b></b></i></div>
<h3 class="f-h" style="left:818px;top:3372px">Need Help?</h3>
<div class="call">✆ CALL US: <strong>1800-555-0199</strong></div>

<div class="f-brand">CALDER ASHBY<small>RECRUITMENT</small></div>
<p class="f-about">Lorem ipsum dolor sit amet, consectetur adipiscing elit. Cras orci sem, vulputate sit amet ipsum vel mi.</p>
<h3 class="f-h" style="left:408px;top:3520px;color:#fff">Information</h3>
<ul class="f-list" style="left:408px;top:3560px"><li>About Us</li><li class="gold">Help Desk</li><li>Support</li><li>Privacy Policy</li><li>Terms &amp; Conditions</li></ul>
<h3 class="f-h" style="left:612px;top:3520px;color:#fff">Useful Links</h3>
<ul class="f-list" style="left:612px;top:3560px"><li>Home</li><li>Search Job</li><li>Positions</li><li>Latest News</li><li class="gold">Jobs</li></ul>
<h3 class="f-h" style="left:820px;top:3520px;color:#fff">Get in Touch</h3>
<div class="contact-form"><div>Name</div><div>Email Address</div><div class="msg">Message<span class="send"><svg width="16" height="16" viewBox="0 0 16 16"><path d="M1 8l14-7-4 14-3-6z" fill="#fff"/></svg></span></div></div>
<div class="rule"></div>
<p class="copy">CALDER ASHBY Copyright © 2017. All rights reserved.</p>

</body>
</html>
```